Exciting business card design for diesel performance and offroad business!!

We need a business card design that looks good and stands out. I don't want a plain old boring business card that you forget about and throw away at the end of the day. We are a diesel performance and truck accessory business that sell and install the industries biggest brands and best parts out there!

Industry/Entity Type

Business

Contact Information for Business Card

Dalton Prewick (Owner) 260-587-3146
bramble.motorworks@postmoor.com
Truck and Off-Road Performance and Accessories

Requirements
Must have
• A great look and feel about it. My logo needs to be in center of the card just like the attached picture. On the back I want it to have a list of items we offer
• Truck and Rovex: Lift and Leveling Kits, Intake and Exhaust Systems, Custom Tuning, Wheels and Tires, Steps, Bed Covers, Floor Liners, Custom Lighting, Turbos and Piping, Gauges, Much More!
• UTV: Suspension, Roll Cage, Doors, Exhaust, Tuning, Turbo Kits, Stereo, Wheels/Tires, Custom Lighting, Clutching, Much More!!

```html
<!DOCTYPE html>
<html lang="en">
<head>
<meta charset="utf-8">
<title>Bramble Motorworks – Business Card</title>
<link rel="stylesheet" href="https://fonts.googleapis.com/css2?family=Oswald:wght@300;400&display=swap">
<style>
  :root {
    --page: #e9e4dc;
    --card: #1d1d1d;
    --card-edge: #262626;
    --band: #6f6f6f;
    --ink: #a9a9a9;
    --ink-strong: #b9b9b9;
  }
  * { box-sizing: border-box; margin: 0; padding: 0; }
  html, body {
    width: 1200px; height: 817px; overflow: hidden;
    background: var(--page);
    font-family: "Oswald", "Arial Narrow", sans-serif;
    font-weight: 300;
    color: var(--ink);
  }
  .card {
    position: absolute; top: 106px;
    width: 385px; height: 607px;
    background: radial-gradient(ellipse at 40% 30%, var(--card-edge), var(--card) 70%);
    box-shadow: 0 4px 12px rgba(0,0,0,.25);
  }
  .card--front { left: 196px; }
  .card--back { left: 619px; }

  .brand {
    position: absolute; left: 0; right: 0; top: 150px;
    text-align: center;
    font-weight: 400; font-size: 34px; line-height: 1.15;
    letter-spacing: 2px; color: var(--band);
    text-transform: uppercase;
  }

  .band {
    position: absolute; left: 0; right: 0;
    display: flex; align-items: center; gap: 12px;
  }
  .band__bar { flex: 1; height: 14px; background: var(--band); }
  .band__label {
    font-weight: 400; font-size: 19px; color: var(--ink-strong);
    white-space: nowrap; letter-spacing: .3px;
  }
  .band--owner { top: 401px; }
  .band--owner .band__bar:first-child { flex: 0 0 115px; }
  .band--truck { top: 92px; }
  .band--utv { top: 379px; }

  .contact {
    position: absolute; left: 0; right: 0; top: 450px;
    text-align: center; font-size: 15px; line-height: 30px;
  }
  .icons {
    position: absolute; top: 562px; left: 0; right: 0; height: 26px;
  }
  .icons svg { position: absolute; top: 0; }

  .offer {
    position: absolute; left: 0; right: 0;
    text-align: center; font-size: 14px; line-height: 23px;
  }
  .offer--truck { top: 146px; }
  .offer--utv { top: 434px; }
  .more { position: absolute; left: 0; right: 0; text-align: center; font-size: 14px; }
  .more--truck { top: 298px; }
  .more--utv { top: 531px; }
</style>
</head>
<body>
  <section class="card card--front">
    <div class="brand">Bramble<br>Motorworks<br>LLC</div>

    <div class="band band--owner">
      <span class="band__bar"></span>
      <span class="band__label">Dalton Prewick [Owner]</span>
      <span class="band__bar"></span>
    </div>

    <div class="contact">
      <p>260-587-3146</p>
      <p>bramble.motorworks@postmoor.com</p>
      <p>Truck and Off-Road Performance and Accessories</p>
    </div>

    <div class="icons">
      <svg style="left:98px" width="28" height="22" viewBox="0 0 28 22" aria-label="Email">
        <rect x="1.5" y="3.5" width="25" height="16" fill="none" stroke="#7a7a7a" stroke-width="1.5"/>
        <path d="M1.5 3.5 L14 13 L26.5 3.5" fill="none" stroke="#7a7a7a" stroke-width="1.5"/>
      </svg>
      <svg style="left:155px" width="16" height="26" viewBox="0 0 16 26" aria-label="Phone">
        <rect x="1.5" y="1" width="13" height="24" rx="2" fill="none" stroke="#7a7a7a" stroke-width="1.5"/>
        <line x1="1.5" y1="20" x2="14.5" y2="20" stroke="#7a7a7a" stroke-width="1.2"/>
      </svg>
      <svg style="left:201px" width="34" height="26" viewBox="0 0 34 26" aria-label="Website">
        <rect x="1" y="1" width="32" height="19" fill="none" stroke="#7a7a7a" stroke-width="1.5"/>
        <line x1="10" y1="24" x2="24" y2="24" stroke="#7a7a7a" stroke-width="1.5"/>
        <line x1="17" y1="20" x2="17" y2="24" stroke="#7a7a7a" stroke-width="1.5"/>
      </svg>
      <svg style="left:265px" width="20" height="20" viewBox="0 0 20 20" aria-label="Social page">
        <rect x="1" y="2" width="18" height="18" fill="#7a7a7a"/>
      </svg>
    </div>
  </section>

  <section class="card card--back">
    <div class="band band--truck">
      <span class="band__bar"></span>
      <span class="band__label">TRUCK AND ROVEX</span>
      <span class="band__bar"></span>
    </div>
    <p class="offer offer--truck">
      Lift and Leveling Kits, Intake and Exhaust<br>
      Systems, Custom Tuning, Wheels and<br>
      Tires, Steps, Bed Covers, Floor Liners,<br>
      Custom Lighting, Turbos and Piping,<br>
      Gauges,
    </p>
    <p class="more more--truck">Much More !!</p>

    <div class="band band--utv">
      <span class="band__bar"></span>
      <span class="band__label">UTV</span>
      <span class="band__bar"></span>
    </div>
    <p class="offer offer--utv">
      Suspension, Roll Cage, Doors, Exhaust,<br>
      Tuning, Turbo Kits, Stereo, Wheels/Tires,<br>
      Custom Lighting, Clutching,
    </p>
    <p class="more more--utv">Much More !!</p>
  </section>
</body>
</html>
```